The Brandling Firm

We need a new design for our letterhead and envelopes. We are a personal injury and criminal defense firm so we need something modern and clean, but more on the professional/traditional side. Our new logo has two colors and is attached to the file so we need something that works well with those colors/matches the design. The following information needs to be on the letterhead:
Phone: (555) 314-2716
Fax: (555) 314-5093
Toll-Free: (800) 555-0143
Post Office Box 4372
Calderton, QV 29548-4372
QVHarmCounselGroup.example
MarrowvaleTrialCounsel.example

Target Market(s)

Clients, government agencies, other law firms

Industry/Entity Type

Legal

Font styles to use
Sans Serif
Other font styles liked:
• Arial

Colors

Designer to choose colors to be used in the design.

Requirements
Must have
• Must look professional and clean, modern
Nice to have
• I would like to see a design that works with the logo but does not distract from the content that will be printed on it
Should not have
• Too many colors or crazy designs.

```html
<!DOCTYPE html>
<html lang="en">
<head>
<meta charset="utf-8">
<title>The Brandling Firm — Letterhead</title>
<link href="https://fonts.googleapis.com/css2?family=Lato:wght@300;400;700&display=swap" rel="stylesheet">
<style>
  :root {
    --backdrop: #4a4a4c;
    --paper: #ffffff;
    --navy: #2e3192;
    --red: #d7262e;
    --rule: #6a6cb8;
    --ink: #2b2b2b;
    --body: #4a4a4a;
    --muted: #5c5c5c;
  }
  * { margin: 0; padding: 0; box-sizing: border-box; }
  html, body {
    width: 1200px; height: 1200px; overflow: hidden;
    background: var(--backdrop);
    font-family: "Lato", Arial, sans-serif;
  }
  .letterhead {
    position: absolute; left: 177px; top: 0;
    width: 847px; height: 1200px;
    background: var(--paper);
  }
  .brand {
    position: absolute; left: 52px; top: 108px;
    display: flex; align-items: center; gap: 9px;
  }
  .brand-mark {
    width: 15px; height: 15px; border-radius: 50%;
    background: var(--red);
  }
  .brand-name {
    font-weight: 700; font-size: 22px; color: var(--navy);
    letter-spacing: 0.3px; white-space: nowrap;
  }
  .header-rule {
    position: absolute; left: 113px; top: 153px;
    width: 678px; height: 1px; background: var(--rule);
  }
  .contact {
    position: absolute; top: 108px;
    font-size: 12.5px; line-height: 18px; color: var(--ink);
    white-space: nowrap;
  }
  .contact-address { left: 318px; }
  .contact-phones { left: 486px; }
  .contact-web { left: 611px; }
  .contact-divider {
    position: absolute; top: 110px; width: 1px; height: 32px;
    background: var(--ink);
  }
  .contact-divider.first { left: 474px; }
  .contact-divider.second { left: 600px; }
  .contact-line { display: flex; align-items: center; gap: 6px; white-space: nowrap; }
  .contact-line svg { width: 11px; height: 11px; flex: none; }
  .toll-free { color: var(--red); }
  .letter {
    position: absolute; left: 85px; top: 340px; width: 683px;
    color: var(--body);
  }
  .salutation { font-size: 17px; color: var(--ink); margin-bottom: 24px; }
  .letter p.body-copy {
    font-weight: 300; font-size: 16.6px; line-height: 27px;
    text-align: justify; hyphens: auto; margin-bottom: 26px;
  }
  .signature {
    position: absolute; left: 90px; top: 874px;
    width: 92px; height: 58px;
    background: linear-gradient(90deg, #e9e9e9, #f6f6f6);
    border-radius: 3px;
  }
  .signer-name {
    position: absolute; left: 85px; top: 954px;
    font-size: 22px; color: var(--ink);
  }
  .signer-title {
    position: absolute; left: 85px; top: 992px;
    font-weight: 300; font-size: 16px; color: var(--muted);
  }
</style>
</head>
<body>
  <main class="letterhead">
    <header>
      <div class="brand">
        <span class="brand-mark"></span>
        <span class="brand-name">The Brandling Firm</span>
      </div>

      <div class="contact contact-address">
        <div>P.O.&nbsp; Box 4372 Calderton</div>
        <div>QV 29548-4372</div>
      </div>
      <span class="contact-divider first"></span>

      <div class="contact contact-phones">
        <div class="contact-line">
          <svg viewBox="0 0 12 12"><path fill="var(--red)" d="M2.5 0.5l2 2.2-1 1.3c0.6 1.4 1.8 2.6 3.3 3.3l1.3-1 2.2 2-1.2 1.9C5 10 1.5 6.6 0.6 1.7z"/></svg>
          <span>(555) 314-2716</span>
        </div>
        <div class="contact-line">
          <svg viewBox="0 0 12 12"><path fill="var(--red)" d="M3 0.5h6v3H3zM1 4h10v5H9v2.5H3V9H1zM4 7.5v3h4v-3z"/></svg>
          <span>(555) 314-5093</span>
        </div>
      </div>
      <span class="contact-divider second"></span>

      <div class="contact contact-web">
        <div class="contact-line">
          <svg viewBox="0 0 12 12"><path fill="var(--red)" d="M2.5 0.5l2 2.2-1 1.3c0.6 1.4 1.8 2.6 3.3 3.3l1.3-1 2.2 2-1.2 1.9C5 10 1.5 6.6 0.6 1.7z"/></svg>
          <span>(800) 555-0143 <span class="toll-free">(Toll-Free)</span></span>
        </div>
        <div class="contact-line">
          <svg viewBox="0 0 12 12" fill="none" stroke="var(--red)" stroke-width="1"><circle cx="6" cy="6" r="5.2"/><ellipse cx="6" cy="6" rx="2.3" ry="5.2"/><path d="M0.8 6h10.4M1.8 3.2h8.4M1.8 8.8h8.4"/></svg>
          <span>QVHarmCounselGroup.example</span>
        </div>
      </div>

      <div class="header-rule"></div>
    </header>

    <section class="letter">
      <p class="salutation">Dear Mr. Smith,</p>
      <p class="body-copy">Lorem ipsum dolor sit amet, consectetur adipiscing elit. Donec orci purus, luctus vitae dignissim eu, iaculis sed purus. Vivamus faucibus, ipsum nec aliquet viverra, leo mauris condimentum ligula, sit amet sagittis enim ligula quis arcu. Nam egestas tortor id nisi porttitor mattis. In tortor ante, ultricies in suscipit a, tempus non massa. Vivamus et auctor mi. Fusce vel massa nulla. Phasellus nec eros mauris, et scelerisque orci. Donec malesuada orci vitae nulla accumsan porta a id massa. Quisque accumsan iaculis magna sit amet fringilla. Maecenas consequat, magna eget tincidunt semper, odio nibh rutrum mi, id feugiat ante nisi eu risus. Vestibulum nunc orci, rhoncus a placerat in, ultricies in mi. Cras mattis varius eros, vel fringilla nisi suscipit eget.</p>
      <p class="body-copy">Quisque scelerisque sagittis nulla at porttitor. Mauris a justo et tellus interdum tristique. Sed id augue vitae urna euismod commodo aliquet a quam. Pellentesque arcu velit, cursus et malesuada ut, consequat et diam. Nullam erat sem, rhoncus id ullamcorper vitae, rhoncus et arcu. In ultricies ultricies nulla, ut rutrum nisi iaculis at. Donec eu magna a metus ornare faucibus. Fusce aliquet faucibus ultricies. Morbi semper, est id tincidunt gravida, sem arcu adipiscing lacus, ac bibendum nulla leo eu purus. Quisque nec diam sed risus consectetur a ccumsan quis quis nibh. Vestibulum id purus lorem.</p>
    </section>

    <div class="signature" role="img" aria-label="Handwritten signature of the sender"></div>
    <p class="signer-name">John Doe</p>
    <p class="signer-title">Co-Founder &amp; CEO</p>
  </main>
</body>
</html>
```